Web Design for Harbor Ledger Allies

Harbor Ledger Allies needs the photoshop files for a simple, clean and professional website design. The company is building a network of bookkeepers/accountants to handle outsourced bookkeeping services for start ups and small businesses. It needs to both attract bookkeepers to become partners and give clients confidence in the professional network. The partners will use products like Tallymint Web, Brightfolio.example and PennyTrim.example for start ups, as well as help with tasks using the clients existing accounting software.

A home and subpage design is needed. I'll award the work based on the home design. The minor subpage changes can be worked out in the workroom stage.

The pages for the navigation will be: Home, Services, Locations, Partners, FAQ, Contact

```html
<!DOCTYPE html>
<html lang="en">
<head>
<meta charset="utf-8">
<title>Harbor Ledger Allies</title>
<link rel="stylesheet" href="https://fonts.googleapis.com/css2?family=Open+Sans:wght@300;400;600&display=swap">
<style>
  :root {
    --brand-blue: #009bdc;
    --slate: #5f6063;
    --slate-text: #c9c9c9;
    --ink: #3a3a3a;
    --white: #ffffff;
    --footer-grey: #c6c6c6;
    --footer-ink: #333333;
    --social: #4a4a4a;
  }
  * { box-sizing: border-box; margin: 0; padding: 0; }
  html, body { width: 960px; height: 1200px; overflow: hidden; }
  body { font-family: "Open Sans", Arial, sans-serif; color: var(--ink); background: var(--white); }

  .site-header { height: 79px; background: var(--brand-blue); position: relative; }
  .brand { position: absolute; left: 58px; top: 17px; color: var(--white); font-weight: 600; font-size: 14px; line-height: 14px; letter-spacing: 0.3px; text-transform: uppercase; }
  .main-nav { position: absolute; top: 46px; left: 0; width: 100%; }
  .main-nav a { position: absolute; color: var(--white); text-decoration: none; font-size: 11.5px; text-transform: uppercase; }

  .hero { height: 358px; background: radial-gradient(ellipse at 55% 45%, #4e87b0 0%, #2a5e86 45%, #173a5a 100%); }

  .why { height: 245px; background: var(--slate); text-align: center; padding-top: 36px; }
  .why h1 { font-weight: 300; font-size: 39px; color: var(--white); line-height: 1.2; }
  .why p { width: 600px; margin: 18px auto 0; font-size: 11.5px; line-height: 13.6px; color: var(--slate-text); }
  .btn { display: inline-block; margin-top: 26px; width: 129px; height: 35px; line-height: 35px; background: var(--brand-blue); color: var(--white); font-size: 12px; text-decoration: none; border-radius: 2px; }

  .services { height: 260px; position: relative; }
  .service { position: absolute; top: 48px; width: 240px; }
  .service .icon { width: 68px; height: 68px; border-radius: 5px; background: var(--brand-blue); margin: 0 auto; display: flex; align-items: center; justify-content: center; }
  .service h2 { font-weight: 400; font-size: 15px; text-align: center; margin-top: 12px; color: #444; }
  .service p { font-size: 10.4px; line-height: 12.6px; margin-top: 15px; color: #333; }

  .partners-band { height: 174px; background: var(--brand-blue); color: var(--white); text-align: center; padding-top: 27px; position: relative; }
  .partners-band .tagline { font-size: 14.5px; line-height: 17.5px; font-weight: 400; }
  .partner-name { position: absolute; top: 103px; transform: translateX(-50%); font-size: 22px; font-weight: 400; white-space: nowrap; display: flex; align-items: center; gap: 10px; }
  .partner-name .dot { width: 30px; height: 30px; border-radius: 50%; background: var(--white); }

  .site-footer { height: 84px; background: var(--footer-grey); position: relative; }
  .footer-brand { position: absolute; left: 102px; top: 27px; font-size: 9px; line-height: 9px; font-weight: 600; color: var(--footer-ink); text-transform: uppercase; }
  .copyright { position: absolute; left: 231px; top: 46px; font-size: 9.6px; color: var(--footer-ink); }
  .footer-nav { position: absolute; left: 364px; top: 46px; font-size: 9.6px; }
  .footer-nav a { color: var(--footer-ink); text-decoration: none; margin-right: 6px; }
  .social { position: absolute; left: 739px; top: 43px; display: flex; gap: 7px; }
  .social span { width: 22px; height: 22px; border-radius: 50%; background: var(--social); }
</style>
</head>
<body>

<header class="site-header">
  <div class="brand">Harbor<br>Ledger<br>Allies</div>
  <nav class="main-nav">
    <a href="#" style="left:409px">Home</a>
    <a href="#" style="left:482px">Services</a>
    <a href="#" style="left:572px">Locations</a>
    <a href="#" style="left:674px">Partners</a>
    <a href="#" style="left:770px">FAQ</a>
    <a href="#" style="left:832px">Contact</a>
  </nav>
</header>

<section class="hero" role="img" aria-label="Photo of a businessman in a suit inspecting a holographic financial chart above a tablet with a magnifying glass"></section>

<section class="why">
  <h1>Why Choose Our Services</h1>
  <p>Beciegast nveriti vitaesaert asety kertya aset aplica binerafae kertyu estyasnemo faserani ptaiades kertyaser daesraeds. Casrolern atur aut oditaut. Binsequuntur magni dolqui ratione volmsequi nesciu orbosas numquam eius modi eincidunt, ut labore et dolore magnam.</p>
  <a href="#" class="btn">read more</a>
</section>

<section class="services">
  <div class="service" style="left:106px">
    <div class="icon">
      <svg width="24" height="32" viewBox="0 0 24 32" fill="#fff"><rect x="0" y="0" width="24" height="32" rx="2"/><rect x="3" y="3" width="18" height="6" fill="#009bdc"/><g fill="#009bdc"><rect x="3" y="12" width="4" height="4"/><rect x="10" y="12" width="4" height="4"/><rect x="17" y="12" width="4" height="4"/><rect x="3" y="19" width="4" height="4"/><rect x="10" y="19" width="4" height="4"/><rect x="17" y="19" width="4" height="4"/><rect x="3" y="26" width="4" height="3"/><rect x="10" y="26" width="4" height="3"/><rect x="17" y="26" width="4" height="3"/></g></svg>
    </div>
    <h2>Accounting</h2>
    <p>Wolore sereledusempquibderumoms odes necessitatibus saepe eveniredums estu Etoluptates estudesu usandaeltaque earumul rerum hic tenetura sapientemi delecut mode.</p>
  </div>
  <div class="service" style="left:370px">
    <div class="icon">
      <svg width="36" height="30" viewBox="0 0 36 30" fill="none" stroke="#fff" stroke-width="2"><rect x="1" y="2" width="9" height="27"/><rect x="13" y="2" width="9" height="27"/><rect x="25" y="3" width="9" height="26" transform="rotate(-10 29 16)"/><circle cx="5.5" cy="23" r="2"/><circle cx="17.5" cy="23" r="2"/></svg>
    </div>
    <h2>Bookkeeping</h2>
    <p>Wolore sereledusempquibderumoms odes necessitatibus saepe eveniredums estu Etoluptates estudesu usandaeltaque earumul rerum hic tenetura sapientemi delecut mode.</p>
  </div>
  <div class="service" style="left:631px">
    <div class="icon">
      <svg width="28" height="30" viewBox="0 0 28 30" fill="none" stroke="#fff" stroke-width="2"><rect x="1" y="4" width="26" height="25" rx="2"/><line x1="1" y1="10" x2="27" y2="10"/><line x1="8" y1="1" x2="8" y2="6"/><line x1="20" y1="1" x2="20" y2="6"/><line x1="9.5" y1="10" x2="9.5" y2="29"/><line x1="18.5" y1="10" x2="18.5" y2="29"/><line x1="1" y1="16.5" x2="27" y2="16.5"/><line x1="1" y1="23" x2="27" y2="23"/></svg>
    </div>
    <h2>Tax Planning</h2>
    <p>Wolore sereledusempquibderumoms odes necessitatibus saepe eveniredums estu Etoluptates estudesu usandaeltaque earumul rerum hic tenetura sapientemi delecut mode.</p>
  </div>
</section>

<section class="partners-band">
  <p class="tagline">Experience and competency in complex numerical manipulations<br>Scrupulous accounting for your business.</p>
  <div class="partner-name" style="left:208px"><span class="dot"></span>Tallymint Web</div>
  <div class="partner-name" style="left:493px">PennyTrim.example</div>
  <div class="partner-name" style="left:764px">Brightfolio.example</div>
</section>

<footer class="site-footer">
  <div class="footer-brand">Harbor<br>Ledger<br>Allies</div>
  <div class="copyright">© Copyright 2014</div>
  <nav class="footer-nav">
    <a href="#">Home</a><a href="#">Services</a><a href="#">Locations</a><a href="#">Partners</a><a href="#">FAQ</a><a href="#">Contact</a><a href="#">Privacy Policy</a><a href="#">Terms</a>
  </nav>
  <div class="social" aria-label="Social links"><span></span><span></span><span></span><span></span></div>
</footer>

</body>
</html>
```